Restoration Specialist in need of business card designs

One side of the business card is a bathroom ripped out down to the studs with just a sink and toilet and then the other side is the bathroom (same sink and toilet) but put back together. Like a before and after on each side behind our information. Stand out, hard to forget, business cards for my restoration company. I want a unique concept all together.
Must include in no particular order:
our business name "Summit Renewals"
Possible Logo for a restoration company
Owner; Dennis Moravec
410-386-7294
dmoravec@summitrenewalsqx.example
SummitRenewalsQX.example (our company website) BUT I am open to any and all designs and options.

Target Market(s)

Customers, Men in the mitigation, plumbing, electrical, HVAC, Roofing, insurance companies

Industry/Entity Type

Restoration/ construction

Contact Information for Business Card

Must include in no particular order: our business name "Summit Renewals" Owner; Dennis Moravec 410-386-7294 dmoravec@summitrenewalsqx.example SummitRenewalsQX.example (our company website) MAY include a list of our services: Residential~ Emergency Response ~ Board- up~ Complete Restoration

Font styles to use
Serif

Colors
0054AA
0677BA
7BADD7
CADEEF
E8F1F8
F0912C
F2A743
F7CA91
FBE8D2
FDF5EE

Requirements
Must have
• unique, memorable, not something men have seen over and over again,
Nice to have
• eye catching
Should not have
• Been something I could have made by myself

```html
<!DOCTYPE html>
<html lang="en">
<head>
<meta charset="utf-8">
<title>Summit Renewals — Business Card</title>
<link href="https://fonts.googleapis.com/css2?family=Noto+Serif:wght@700&family=Arimo:wght@400&display=swap" rel="stylesheet">
<style>
  :root {
    --navy: #0f3049;
    --orange: #e06d22;
    --ink: #2a2a2a;
    --card: #ededed;
    --backdrop: #dedede;
  }
  * { margin: 0; padding: 0; box-sizing: border-box; }
  html, body { width: 1200px; height: 1124px; overflow: hidden; }
  body {
    background: var(--backdrop);
    font-family: "Arimo", Arial, sans-serif;
    color: var(--ink);
    position: relative;
  }
  .card {
    position: absolute;
    left: 252px;
    width: 696px;
    height: 398px;
    background: var(--card);
    border-radius: 28px;
    overflow: hidden;
  }
  .card--front { top: 134px; }
  .card--back { top: 592px; }

  .wordmark {
    font-family: "Noto Serif", Georgia, serif;
    font-weight: 700;
    color: var(--orange);
    text-align: center;
    line-height: 1.05;
  }
  .card--front .wordmark {
    position: absolute;
    left: 78px;
    top: 122px;
    width: 200px;
    font-size: 34px;
  }
  .divider {
    position: absolute;
    left: 280px;
    top: 115px;
    width: 1.5px;
    height: 167px;
    background: var(--navy);
  }
  .contact {
    position: absolute;
    left: 309px;
    top: 115px;
  }
  .contact__name {
    font-family: "Noto Serif", Georgia, serif;
    font-weight: 700;
    font-size: 28px;
    letter-spacing: 0.3px;
    color: var(--navy);
    line-height: 1.1;
  }
  .contact__name .surname { color: var(--orange); }
  .contact__role { font-size: 17px; margin-top: 0; }
  .contact__list { list-style: none; margin-top: 36px; }
  .contact__list li {
    display: flex;
    align-items: center;
    font-size: 17px;
    height: 27.5px;
  }
  .contact__list svg { width: 13px; height: 13px; margin-right: 7px; flex: none; }

  .wave { position: absolute; left: 0; bottom: 0; width: 696px; height: 70px; }

  .card--back .wordmark {
    position: absolute;
    left: 0;
    top: 118px;
    width: 100%;
    font-size: 58px;
  }
  .services {
    position: absolute;
    left: 0;
    top: 312px;
    width: 100%;
    text-align: center;
    font-size: 17px;
    line-height: 25px;
  }
  .services .dot { color: var(--orange); margin: 0 4px 0 8px; font-size: 12px; vertical-align: 2px; }
</style>
</head>
<body>

<section class="card card--front">
  <div class="wordmark">Summit<br>Renewals</div>
  <div class="divider"></div>
  <div class="contact">
    <h1 class="contact__name">DENNIS <span class="surname">MORAVEC</span></h1>
    <p class="contact__role">Owner</p>
    <ul class="contact__list">
      <li>
        <svg viewBox="0 0 24 24" aria-hidden="true"><path fill="var(--orange)" d="M6.6 10.8a15 15 0 0 0 6.6 6.6l2.2-2.2a1 1 0 0 1 1-.25 11.4 11.4 0 0 0 3.6.6 1 1 0 0 1 1 1V20a1 1 0 0 1-1 1A17 17 0 0 1 3 4a1 1 0 0 1 1-1h3.5a1 1 0 0 1 1 1c0 1.25.2 2.45.6 3.6a1 1 0 0 1-.25 1z"/></svg>
        410-386-7294
      </li>
      <li>
        <svg viewBox="0 0 24 24" aria-hidden="true"><rect x="2" y="5" width="20" height="14" fill="var(--orange)"/><path d="M2 5l10 8 10-8" fill="none" stroke="var(--card)" stroke-width="1.8"/></svg>
        dmoravec@summitrenewalsqx.example
      </li>
      <li>
        <svg viewBox="0 0 24 24" aria-hidden="true"><g fill="none" stroke="var(--orange)" stroke-width="2"><circle cx="12" cy="12" r="10"/><ellipse cx="12" cy="12" rx="4.5" ry="10"/><path d="M2 12h20M4 7h16M4 17h16"/></g></svg>
        www.SummitRenewalsQX.example
      </li>
    </ul>
  </div>
  <svg class="wave" viewBox="0 0 696 70" preserveAspectRatio="none" aria-hidden="true">
    <path d="M0 0 Q348 92 696 0 V70 H0 Z" fill="var(--navy)"/>
    <path d="M50 10 Q348 68 646 10 Q348 63 50 10 Z" fill="var(--orange)" stroke="var(--card)" stroke-width="1"/>
  </svg>
</section>

<section class="card card--back">
  <div class="wordmark">Summit Renewals</div>
  <p class="services">
    Residential <span class="dot">●</span>Emergency Response <span class="dot">●</span>Board- up <span class="dot">●</span>Storm Protection<br>
    Complete Restoration
  </p>
</section>

</body>
</html>
```